Fernvale Business Card Design

We are looking for a fresh business card design for our new logo. We would like a business card that is unique but friendly. We are in the window coverings business offering blinds, shutters and shades for homes.

Target Market(s)

Targeting the end-consumer

Industry/Entity Type

Business

Requirements
Must have
• Must have a dedicates space for a photo of our sales person. Must contain our new logo (attached).

```html
<!DOCTYPE html>
<html lang="en">
<head>
<meta charset="utf-8">
<title>Fernvale Business Card</title>
<link rel="stylesheet" href="https://fonts.googleapis.com/css2?family=Open+Sans:wght@400;600;700&display=swap">
<style>
  :root {
    --page: #e9eaea;
    --card: #f7f8f7;
    --card-edge: #9a9c9b;
    --ink: #2f3132;
    --ink-soft: #3c3e3f;
    --green: #5b9d1f;
    --rule: #8e9091;
    --photo-top: #b9bcbd;
    --photo-bottom: #6f8250;
  }
  * { box-sizing: border-box; margin: 0; padding: 0; }
  html, body {
    width: 1200px; height: 970px; overflow: hidden;
    background: var(--page);
    font-family: "Open Sans", Arial, sans-serif;
    color: var(--ink);
  }
  .card {
    position: absolute; left: 100px; top: 207px;
    width: 1000px; height: 556px;
    background: var(--card);
    border: 1.5px solid var(--card-edge);
    border-radius: 54px;
  }
  .brand {
    position: absolute; left: 52px; top: 86px;
    display: flex; align-items: center; gap: 22px;
  }
  .brand-mark {
    width: 92px; height: 92px;
    border: 4px solid var(--ink-soft);
    border-radius: 6px;
  }
  .brand-name {
    font-size: 66px; font-weight: 400; color: var(--ink-soft);
    letter-spacing: 0.5px; line-height: 1;
  }
  .photo {
    position: absolute; left: 805px; top: 102px;
    width: 146px; height: 135px;
    border: 6px solid var(--green);
    border-radius: 4px 26px 4px 26px;
    background: linear-gradient(180deg, var(--photo-top), var(--photo-bottom));
  }
  .person {
    position: absolute; right: 49px; top: 262px; text-align: right;
  }
  .person-name {
    font-size: 30px; font-weight: 700; color: var(--green);
    letter-spacing: 0.6px; line-height: 1.2;
  }
  .person-role { font-size: 22px; color: var(--ink); line-height: 1.3; }
  .rule {
    position: absolute; top: 344px; height: 0;
  }
  .rule-grey { left: 48px; width: 615px; border-top: 1.5px solid var(--rule); }
  .rule-green { left: 663px; width: 288px; border-top: 2.5px solid var(--green); }
  .contacts {
    position: absolute; left: 52px; top: 368px; list-style: none;
  }
  .contacts li {
    display: flex; align-items: center; gap: 10px;
    font-size: 22px; line-height: 34.5px; color: var(--ink);
  }
  .contacts svg { width: 22px; height: 22px; fill: var(--green); flex: none; }
  .address {
    position: absolute; right: 49px; top: 420px; text-align: right;
    font-size: 22px; line-height: 30px; color: var(--ink); font-style: normal;
  }
</style>
</head>
<body>
  <main class="card">
    <div class="brand">
      <span class="brand-mark"></span>
      <span class="brand-name">Fernvale</span>
    </div>

    <div class="photo" role="img" aria-label="Portrait photo of the sales representative"></div>

    <div class="person">
      <p class="person-name">MAREN ASHBY</p>
      <p class="person-role">Managing Director</p>
    </div>

    <div class="rule rule-grey"></div>
    <div class="rule rule-green"></div>

    <ul class="contacts">
      <li>
        <svg viewBox="0 0 24 24" aria-hidden="true"><path d="M7 1h10a2 2 0 0 1 2 2v18a2 2 0 0 1-2 2H7a2 2 0 0 1-2-2V3a2 2 0 0 1 2-2zm0 3v12h10V4zm5 14.2a1.3 1.3 0 1 0 0 2.6 1.3 1.3 0 0 0 0-2.6z"/></svg>
        <span>+ 000 000 0000</span>
      </li>
      <li>
        <svg viewBox="0 0 24 24" aria-hidden="true"><path d="M2 8c0-3 4-5 10-5s10 2 10 5v2h-5V8H7v2H2zm4 4h12l3 9H3zm6 2a3 3 0 1 0 0 6 3 3 0 0 0 0-6z"/></svg>
        <span>+ 000 000 0000</span>
      </li>
      <li>
        <svg viewBox="0 0 24 24" aria-hidden="true"><path d="M2 5h20v14H2zm2 2v.4l8 5.6 8-5.6V7zm0 2.8V17h16V9.8l-8 5.6z"/></svg>
        <span>hello@fernvale.com</span>
      </li>
      <li>
        <svg viewBox="0 0 24 24" aria-hidden="true"><path d="M12 2a10 10 0 1 0 0 20 10 10 0 0 0 0-20zm0 2c1.2 0 2.5 2.2 3 6H9c.5-3.8 1.8-6 3-6zM4.3 10h2.7a20 20 0 0 1 .4-4.6A8 8 0 0 0 4.3 10zm12.7 0h2.7a8 8 0 0 0-3.1-4.6c.3 1.4.4 3 .4 4.6zM4.3 12h2.7c0 1.7.1 3.2.4 4.6A8 8 0 0 1 4.3 12zm4.7 0h6c-.5 4-1.8 6-3 6s-2.5-2-3-6zm8 0h2.7a8 8 0 0 1-3.1 4.6c.3-1.4.4-2.9.4-4.6z"/></svg>
        <span>www.fernvale.com</span>
      </li>
    </ul>

    <address class="address">
      Level 12, 8 Harbour Lane<br>
      Sydney, 20, New South Wales
    </address>
  </main>
</body>
</html>
```